Business cards real estate company

We need a design for a business card. It is a company that specializes in real estate sales. There should be space for a photo of the respective employee as well as the website and telephone number on it. Design should be noble, innovative.

Contact Information for Business Card

Website, Name, Position, Telefonnummer

Requirements
Must have
• Photo, logo

```html
<!DOCTYPE html>
<html lang="en">
<head>
<meta charset="utf-8">
<title>Casavera – Business Card</title>
<link rel="stylesheet" href="https://fonts.googleapis.com/css2?family=Montserrat:wght@600;700&family=Arimo:wght@400&display=swap">
<style>
  :root {
    --lime: #bdd92f;
    --green: #76bb42;
    --white: #ffffff;
    --photo-bg: #f0f0f0;
    --photo-tone: #85888b;
    --stage: #2b2b2b;
  }
  * { margin: 0; padding: 0; box-sizing: border-box; }
  html, body { width: 1200px; height: 1015px; overflow: hidden; background: var(--stage); }
  .canvas { position: relative; width: 1200px; height: 1015px; }
  .card {
    position: absolute; left: 200px; width: 800px; height: 457px;
    overflow: hidden; box-shadow: 0 10px 30px rgba(0,0,0,.45);
  }
  .card__art { position: absolute; inset: 0; display: block; }
  .card--front { top: 28px; }
  .card--back { top: 528px; }
  .brand {
    position: absolute; left: 0; top: 190px; width: 690px; text-align: center;
    font-family: "Montserrat", sans-serif; font-weight: 600; font-size: 74px;
    letter-spacing: 1px; color: var(--lime); line-height: 1;
  }
  .contact {
    position: absolute; left: 70px; top: 262px; color: var(--white);
    font-family: "Arimo", sans-serif;
  }
  .contact__name {
    font-family: "Montserrat", sans-serif; font-weight: 700; font-size: 29px;
    letter-spacing: .5px; line-height: 1.05;
  }
  .contact__role { font-size: 22px; margin-top: 2px; }
  .contact__list { list-style: none; margin-top: 24px; font-size: 21px; }
  .contact__list li { display: flex; align-items: center; gap: 10px; margin-bottom: 6px; }
  .contact__icon { width: 20px; height: 20px; flex: none; display: block; }
</style>
</head>
<body>
<main class="canvas">

  <section class="card card--front" aria-label="Card front">
    <svg class="card__art" viewBox="0 0 800 457" width="800" height="457" aria-hidden="true">
      <rect width="800" height="457" fill="var(--lime)"/>
      <path d="M0 0 H400 C640 0 740 150 700 300 C680 380 640 430 610 457 H0 Z" fill="var(--white)"/>
      <path d="M450 6 C660 10 760 160 715 310 C695 380 660 420 630 450" fill="none" stroke="var(--green)" stroke-width="3"/>
    </svg>
    <div class="brand">Casavera</div>
  </section>

  <section class="card card--back" aria-label="Card back">
    <svg class="card__art" viewBox="0 0 800 457" width="800" height="457">
      <rect width="800" height="457" fill="var(--green)"/>
      <circle cx="600" cy="190" r="245" fill="var(--white)"/>
      <path d="M440 40 C350 150 360 340 540 445" fill="none" stroke="var(--lime)" stroke-width="4"/>
      <circle cx="600" cy="200" r="165" fill="var(--photo-bg)"/>
      <circle cx="600" cy="200" r="145" fill="var(--photo-tone)" role="img" aria-label="Portrait photo of the employee"/>
    </svg>
    <div class="contact">
      <div class="contact__name">MARCUS KELLER</div>
      <div class="contact__role">Managing Director</div>
      <ul class="contact__list">
        <li>
          <svg class="contact__icon" viewBox="0 0 24 24" aria-hidden="true"><path d="M6.6 10.8a15 15 0 0 0 6.6 6.6l2.2-2.2c.3-.3.7-.4 1-.2 1.1.4 2.3.6 3.6.6.6 0 1 .4 1 1V20c0 .6-.4 1-1 1A17 17 0 0 1 3 4c0-.6.4-1 1-1h3.5c.6 0 1 .4 1 1 0 1.3.2 2.5.6 3.6.1.3 0 .7-.2 1z" fill="#fff"/></svg>
          044-987 654 321
        </li>
        <li>
          <svg class="contact__icon" viewBox="0 0 24 24" aria-hidden="true"><g fill="none" stroke="#fff" stroke-width="2"><circle cx="12" cy="12" r="9.5"/><ellipse cx="12" cy="12" rx="4" ry="9.5"/><path d="M2.5 12h19M4 7h16M4 17h16"/></g></svg>
          www.casavera-homes.com
        </li>
      </ul>
    </div>
  </section>

</main>
</body>
</html>
```